Harborline Motors LLC

Car Dealer Customer Service
Address: 2741 Linden Avenue, Shelbyville, TN 37162
web: www.harborlinemotorstn.net
email: harborlinemotorstn@mailbox-example.net
Phone: (931) 555-0148
Phone: (629) 555-0173

```html
<!DOCTYPE html>
<html lang="en">
<head>
<meta charset="utf-8">
<title>Harborline Motors – Business Cards</title>
<link href="https://fonts.googleapis.com/css2?family=Poppins:wght@400;500;700;800&display=swap" rel="stylesheet">
<style>
  :root {
    --blue: #2b8fcc;
    --blue-deep: #1f6fa8;
    --gold: #e9b548;
    --ink: #1d1d1d;
    --paper: #ffffff;
    --backdrop: #cfcfcf;
  }
  * { margin: 0; padding: 0; box-sizing: border-box; }
  html, body { width: 1200px; height: 852px; overflow: hidden; }
  body {
    background: var(--backdrop);
    font-family: "Poppins", sans-serif;
    position: relative;
  }
  .card {
    position: absolute;
    top: 256px;
    width: 540px;
    height: 310px;
    background: var(--paper);
    box-shadow: 0 6px 18px rgba(0,0,0,.25);
    overflow: hidden;
  }
  .card--front { left: 40px; }
  .card--back { left: 620px; }

  /* Front */
  .front-brand {
    position: absolute; left: 0; right: 0; top: 52px;
    display: flex; flex-direction: column; align-items: center; gap: 16px;
  }
  .brand-dot {
    width: 90px; height: 90px; border-radius: 50%;
    background: var(--gold);
    flex: none;
  }
  .brand-name {
    color: var(--blue-deep);
    font-weight: 800;
    font-size: 28px;
    letter-spacing: .5px;
    text-transform: uppercase;
  }
  .front-rule {
    position: absolute; left: 0; right: 0; bottom: 60px;
    height: 3px; background: var(--gold);
  }
  .front-band {
    position: absolute; left: 0; right: 0; bottom: 0; height: 56px;
    background: var(--blue);
    display: flex; align-items: center; justify-content: center;
  }
  .front-band .ghost {
    position: absolute; left: 24px; top: 10px;
    width: 36px; height: 36px; border-radius: 50%;
    background: rgba(255,255,255,.18);
  }
  .front-web {
    color: #fff; font-size: 13px; font-weight: 500; letter-spacing: 2px;
    text-transform: uppercase;
  }

  /* Back */
  .back-band {
    position: absolute; left: 0; right: 0; top: 0; height: 78px;
    background: linear-gradient(90deg, var(--gold) 0%, var(--gold) 24%, var(--blue) 52%, var(--blue) 100%);
    display: flex; align-items: center; justify-content: flex-end;
    padding-right: 26px;
  }
  .back-title {
    color: #fff; font-weight: 800; font-size: 26px; text-transform: uppercase;
    letter-spacing: .5px;
  }
  .back-tab {
    position: absolute; left: 0; top: 78px; width: 230px; height: 40px;
    background: linear-gradient(90deg, var(--gold) 60%, rgba(233,181,72,0) 100%);
  }
  .role {
    position: absolute; left: 26px; top: 130px;
    font-weight: 700; font-size: 15px; color: var(--ink);
    text-transform: uppercase;
  }
  .divider {
    position: absolute; left: 26px; width: 250px; height: 1px; background: #9a9a9a;
  }
  .divider--top { top: 160px; }
  .divider--bottom { top: 272px; }
  .contacts {
    position: absolute; left: 26px; top: 170px; width: 300px;
    list-style: none; display: flex; flex-direction: column; gap: 6px;
  }
  .contacts li {
    display: flex; align-items: center; gap: 8px;
    font-size: 12px; color: var(--ink); white-space: nowrap;
  }
  .contacts svg { width: 13px; height: 13px; flex: none; }
  .address {
    position: absolute; left: 26px; top: 280px;
    font-size: 12px; color: var(--ink);
  }
  .back-brand {
    position: absolute; right: 24px; top: 100px; width: 170px;
    display: flex; flex-direction: column; align-items: center; gap: 10px;
    text-align: center;
  }
  .back-brand .brand-dot { width: 100px; height: 100px; }
  .back-brand .brand-name { font-size: 16px; line-height: 1.3; }
</style>
</head>
<body>

  <section class="card card--front" aria-label="Card front">
    <div class="front-brand">
      <span class="brand-dot"></span>
      <span class="brand-name">Harborline Motors</span>
    </div>
    <div class="front-rule"></div>
    <div class="front-band">
      <span class="ghost"></span>
      <span class="front-web">www.harborlinemotorstn.net</span>
    </div>
  </section>

  <section class="card card--back" aria-label="Card back">
    <div class="back-band">
      <span class="back-title">Harborline Motors</span>
    </div>
    <div class="back-tab"></div>
    <p class="role">Car Dealer Customer Service</p>
    <div class="divider divider--top"></div>
    <ul class="contacts">
      <li>
        <svg viewBox="0 0 24 24" aria-hidden="true"><path fill="var(--gold)" d="M6.6 10.8a15 15 0 0 0 6.6 6.6l2.2-2.2a1 1 0 0 1 1-.25 11.4 11.4 0 0 0 3.6.57 1 1 0 0 1 1 1V20a1 1 0 0 1-1 1A17 17 0 0 1 3 4a1 1 0 0 1 1-1h3.5a1 1 0 0 1 1 1c0 1.25.2 2.45.57 3.57a1 1 0 0 1-.25 1z"/></svg>
        (931) 555-0148
      </li>
      <li>
        <svg viewBox="0 0 24 24" aria-hidden="true"><path fill="var(--gold)" d="M6.6 10.8a15 15 0 0 0 6.6 6.6l2.2-2.2a1 1 0 0 1 1-.25 11.4 11.4 0 0 0 3.6.57 1 1 0 0 1 1 1V20a1 1 0 0 1-1 1A17 17 0 0 1 3 4a1 1 0 0 1 1-1h3.5a1 1 0 0 1 1 1c0 1.25.2 2.45.57 3.57a1 1 0 0 1-.25 1z"/></svg>
        (629) 555-0173
      </li>
      <li>
        <svg viewBox="0 0 24 24" aria-hidden="true"><circle cx="12" cy="12" r="9" fill="none" stroke="var(--gold)" stroke-width="2"/><path d="M3 12h18M12 3c3 3 3 15 0 18M12 3c-3 3-3 15 0 18" fill="none" stroke="var(--gold)" stroke-width="2"/></svg>
        www.harborlinemotorstn.net
      </li>
      <li>
        <svg viewBox="0 0 24 24" aria-hidden="true"><rect x="2" y="5" width="20" height="14" fill="var(--gold)"/><path d="M2 5l10 8 10-8" fill="none" stroke="#fff" stroke-width="2"/></svg>
        harborlinemotorstn@mailbox-example.net
      </li>
    </ul>
    <div class="divider divider--bottom"></div>
    <p class="address">2741 Linden Avenue, Shelbyville, TN 37162</p>
    <div class="back-brand">
      <span class="brand-dot"></span>
      <span class="brand-name">Harborline Motors</span>
    </div>
  </section>

</body>
</html>
```